I need a bushiness card designed for my business Kind Sparrow Club attached is the logo
On the business cards I would like the following info
427 Hollister Ln #3085
Spring Tx, 77519
936-481-5527
Please free free to be creative, our business targets girls 6-11 years old, a hip and cool looking card is what we are looking for to be passed out at a girls event.......Thanks

```html
<!DOCTYPE html>
<html lang="en">
<head>
<meta charset="utf-8">
<title>Kind Sparrow Club – Business Card</title>
<link rel="stylesheet" href="https://fonts.googleapis.com/css2?family=Roboto:wght@400;700&display=swap">
<style>
  :root {
    --backdrop: #a9dccf;
    --sky-light: #8fe3f2;
    --sky-mid: #4cc3e0;
    --sky-deep: #2a9fc2;
    --navy: #1d3a52;
    --navy-deep: #152c40;
    --pink: #e2267f;
    --coral: #ef5a7e;
    --cyan: #3fc6e6;
    --violet: #7b3f9a;
    --soft-white: #eef3f5;
    --art-tone: #3b6fa8;
  }
  * { box-sizing: border-box; margin: 0; padding: 0; }
  html, body { width: 1200px; height: 856px; overflow: hidden; }
  body {
    background: var(--backdrop);
    font-family: "Roboto", Arial, sans-serif;
    display: flex;
    flex-direction: column;
    align-items: center;
    justify-content: center;
    gap: 56px;
  }
  .card {
    position: relative;
    width: 560px;
    height: 320px;
    border-radius: 26px;
    overflow: hidden;
    box-shadow: 0 6px 18px rgba(20, 60, 70, 0.18);
  }

  /* Back side: contact details */
  .card--back {
    background: linear-gradient(160deg, var(--navy) 0%, var(--navy-deep) 100%);
  }
  .contact-list {
    position: absolute;
    left: 40px;
    top: 46px;
    list-style: none;
    display: flex;
    flex-direction: column;
    gap: 14px;
  }
  .contact-item {
    display: flex;
    align-items: flex-start;
    gap: 14px;
    color: var(--coral);
    font-size: 25px;
    line-height: 1.2;
  }
  .contact-item svg { flex: none; width: 22px; height: 22px; margin-top: 4px; }
  .contact-item .address { display: flex; flex-direction: column; gap: 6px; }
  .back-name {
    position: absolute;
    right: 34px;
    top: 40px;
    width: 150px;
    text-align: right;
    color: var(--pink);
    font-weight: 700;
    font-size: 34px;
    line-height: 1.05;
  }

  /* Front side: brand */
  .card--front {
    background: radial-gradient(circle at 62% 48%, var(--sky-light) 0%, var(--sky-mid) 48%, var(--sky-deep) 100%);
  }
  .front-name {
    position: absolute;
    left: 36px;
    top: 70px;
    width: 250px;
    color: var(--pink);
    font-weight: 700;
    font-size: 50px;
    line-height: 1.02;
  }
  .front-art {
    position: absolute;
    left: 300px;
    top: 40px;
    width: 220px;
    height: 190px;
    border-radius: 18px;
    background: linear-gradient(150deg, var(--art-tone) 0%, var(--sky-mid) 100%);
    opacity: 0.55;
  }
  .front-link {
    position: absolute;
    left: 36px;
    bottom: 22px;
    color: var(--soft-white);
    font-size: 27px;
    letter-spacing: 0.2px;
  }
</style>
</head>
<body>

  <section class="card card--back" aria-label="Card back with contact details">
    <ul class="contact-list">
      <li class="contact-item">
        <svg viewBox="0 0 24 24" aria-hidden="true"><path fill="var(--cyan)" d="M6.6 10.8a15.1 15.1 0 0 0 6.6 6.6l2.2-2.2a1 1 0 0 1 1-.25 11.4 11.4 0 0 0 3.6.57 1 1 0 0 1 1 1V20a1 1 0 0 1-1 1A17 17 0 0 1 3 4a1 1 0 0 1 1-1h3.5a1 1 0 0 1 1 1c0 1.25.2 2.45.57 3.6a1 1 0 0 1-.25 1z"/></svg>
        <span>936-481-5527</span>
      </li>
      <li class="contact-item">
        <svg viewBox="0 0 24 24" aria-hidden="true"><g fill="none" stroke="var(--cyan)" stroke-width="2.4" stroke-linecap="round"><path d="M10 14a4 4 0 0 0 5.7 0l3.5-3.5a4 4 0 0 0-5.7-5.7l-1.2 1.2"/><path d="M14 10a4 4 0 0 0-5.7 0l-3.5 3.5a4 4 0 0 0 5.7 5.7l1.2-1.2"/></g></svg>
        <span>www.kindsparrowclub.net</span>
      </li>
      <li class="contact-item">
        <svg viewBox="0 0 24 24" aria-hidden="true"><path fill="var(--cyan)" d="M4 4h16a2 2 0 0 1 2 2v9a2 2 0 0 1-2 2H9l-5 4v-4a2 2 0 0 1-2-2V6a2 2 0 0 1 2-2z"/></svg>
        <span>friendpage.com/kindsparrowclub</span>
      </li>
      <li class="contact-item">
        <svg viewBox="0 0 24 24" aria-hidden="true"><path fill="var(--cyan)" d="M12 2a7 7 0 0 0-7 7c0 5.2 7 13 7 13s7-7.8 7-13a7 7 0 0 0-7-7zm0 9.5A2.5 2.5 0 1 1 12 6.5a2.5 2.5 0 0 1 0 5z"/></svg>
        <span class="address"><span>427 Hollister Ln #3085</span><span>Spring Tx, 77519</span></span>
      </li>
    </ul>
    <p class="back-name">Kind Sparrow Club</p>
  </section>

  <section class="card card--front" aria-label="Card front with club name">
    <p class="front-name">Kind Sparrow Club</p>
    <div class="front-art" role="img" aria-label="Illustration of a cartoon girl with a red heart on a sunburst background"></div>
    <p class="front-link">friendpage.com/kindsparrowclub</p>
  </section>

</body>
</html>
```